依頼詳細
◇サイトマップ
①ホーム
②コンセプト
③施設紹介・アクセス
④サービス紹介
⑤一日の流れ
⑥利用までの流れ
⑦ご利用料金
⑧イベント
⑨ケアマネージャー様へ
⑩採用情報
⑪会社概要
⑫Blog(一覧)
⑬News(一覧)
⑭ご利用者さまの声
⑮よくある質問
⑯お問い合わせ

◇構成
最近多い、縦長構成のサイトが嫌いです。
可愛くて動きの多いサイトを希望しています。
参考サイト:http://pipomo-tanta.jp/
ここのサイトの画像が縦に流れていく動きがすごく好きなので、
これは必ずやりたいです。

◇優先事項
1.凝ったデザイン
2.ユーザビリティー
3.編集更新

◇期待する効果
1.新規顧客の獲得
2.売上の向上
3.認知度の向上

◇ターゲット
【性別】男女比(男 4:6 女)
【年代】30代~50代 ※本人に見てもらうのではなく娘さん・息子さんやケアマネージャーの方に見てもらうことを想定しています。
【属性】会社員 自営業 主婦

◇テイスト
◯可愛い・キュート カジュアル ポップ
×クール エレガント パステル 重厚感 幻想的・神秘的 高級感

サイトURL
http://www.hkv-lavande-orme.com
ページ数
1ページ
希望イメージ
シンプル 複雑
単色 カラフル
暗い 明るい
日常 高級
遊び心 厳粛
未来的 伝統的
女性的 男性的
希望する色
赤系、茶系、上のカラーチャートにある、赤系の右から3番目の赤とピンクの間ぐらいの色が好きです。 茶系の色も好きで
補足説明
店内写真などをクラウドボックスを使って、アップしています。
下記URLよりダウンロードしてください。
■ダウンロードURL
http://cloudbox-example.jp/download/8ac41e7d03b96f25e1d7c0b3a95f4e18d62c7b09
ダウンロードパスワード pass

素材➁
picvault:http://picvault-example.com/
ガゾーナ:https://jp.gazona-example.com/
当院で定期契約をしています。クレジット購入のみのもの以外をご利用下さい。
また定期契約のものは当院の負担となり、ワーカー様に負担はありません。
カンプ画像を入れてください。

素材③
現行サイトより引用してください。

```html
<!DOCTYPE html>
<html lang="ja">
<head>
<meta charset="utf-8">
<title>デイサービスセンター はるいろ</title>
<link href="https://fonts.googleapis.com/css2?family=M+PLUS+Rounded+1c:wght@400;700&display=swap" rel="stylesheet">
<style>
:root{
  --pink:#f3798a;
  --pink-dark:#e5606f;
  --pink-soft:#fde3e6;
  --brown:#6b4a3a;
  --brown-light:#9a8073;
  --beige:#f8f3ea;
  --white:#ffffff;
  --sky-top:#8cc7ec;
  --sky-bottom:#e9f5fb;
  --line:#ece3d8;
}
*{box-sizing:border-box;margin:0;padding:0}
html,body{width:1200px;height:2800px;overflow:hidden}
body{font-family:"M PLUS Rounded 1c",sans-serif;color:var(--brown);background:var(--white);font-size:14px}
a{color:inherit;text-decoration:none}

/* hero */
.hero{position:relative;height:840px;display:flex}
.sidebar{width:220px;background:var(--white);position:relative;z-index:2;padding:28px 0 0}
.brand{display:flex;flex-direction:column;align-items:center;gap:8px;margin-bottom:40px}
.brand-dot{width:44px;height:44px;border-radius:50%;background:var(--pink)}
.brand-name{font-size:15px;font-weight:700;color:var(--pink)}
.global-nav li{list-style:none;border-bottom:1px solid var(--line)}
.global-nav a{display:block;padding:13px 22px;font-size:14px;font-weight:700}
.contact-box{position:absolute;left:0;right:0;top:560px;bottom:0;background:var(--pink);color:var(--white);padding:24px 18px;text-align:center}
.contact-illust{width:64px;height:64px;border-radius:50%;background:var(--pink-soft);margin:0 auto 12px}
.contact-note{font-size:11px;line-height:1.6;margin-bottom:10px}
.contact-tel{display:flex;align-items:center;justify-content:center;gap:6px;font-size:20px;font-weight:700;margin-bottom:14px}
.contact-btn{display:inline-block;background:var(--white);color:var(--pink);border-radius:20px;padding:8px 26px;font-size:13px;font-weight:700}

.hero-visual{flex:1;position:relative;background:linear-gradient(var(--sky-top),var(--sky-bottom) 70%,#f4f1ec)}
.hero-illust{position:absolute;left:150px;top:140px;width:420px;height:560px;border-radius:24px;background:linear-gradient(#c9b7a2,#e7d9c6 60%,#f0e6d8)}
.scroll-mark{position:absolute;left:330px;bottom:40px;width:60px;text-align:center;font-size:10px;color:var(--pink)}
.scroll-mark span{display:block;width:40px;height:40px;margin:0 auto 4px;border-radius:50%;border:2px solid var(--pink)}

.menu-cards{position:absolute;right:32px;top:20px;display:flex;flex-direction:column;gap:12px}
.menu-card{width:280px;height:122px;background:var(--pink);border-radius:6px;display:flex;overflow:hidden;color:var(--white)}
.menu-card-thumb{width:110px;background:var(--pink-soft)}
.menu-card-body{flex:1;padding:18px 14px;display:flex;flex-direction:column;justify-content:center}
.menu-card-en{font-size:11px;opacity:.85}
.menu-card-title{font-size:19px;font-weight:700;margin:2px 0 8px}
.menu-card-more{font-size:11px;align-self:flex-end}

/* greeting */
.greeting{height:700px;background:var(--beige);text-align:center;padding-top:90px}
.section-title{font-size:30px;font-weight:700;color:var(--pink);letter-spacing:.08em}
.section-title::after{content:"";display:block;width:40px;height:3px;background:var(--pink);margin:14px auto 0;border-radius:2px}
.greeting-text{margin:44px auto 0;width:640px;font-size:14px;line-height:2.3}
.greeting-photos{display:flex;justify-content:center;gap:36px;margin-top:54px}
.greeting-photo{width:160px;height:160px;border-radius:50%;border:5px solid var(--white);box-shadow:0 0 0 2px var(--pink)}

/* news */
.news{height:540px;padding-top:70px;text-align:center}
.news-list{display:flex;justify-content:center;gap:28px;margin-top:46px}
.news-item{width:232px;text-align:left}
.news-thumb{height:150px;background:linear-gradient(#9fcf86,#d9ecc9)}
.news-text{font-size:12px;line-height:1.7;margin-top:10px}
.news-date{font-size:11px;color:var(--brown-light);margin-top:6px}
.news-actions{display:flex;justify-content:center;gap:24px;margin-top:40px}
.pill-btn{background:var(--pink);color:var(--white);border-radius:22px;padding:10px 34px;font-size:13px;font-weight:700}

/* access */
.access{height:400px;background:var(--beige);padding-top:60px;text-align:center}
.access-body{display:flex;justify-content:center;gap:40px;margin-top:36px}
.access-map{width:440px;height:210px;background:linear-gradient(135deg,#e6e4dc,#d5dbe0)}
.access-table{width:420px;border-collapse:collapse;text-align:left;font-size:12px}
.access-table th{width:90px;font-weight:700;padding:4px 0;color:var(--pink)}
.access-table td{padding:4px 0;border-bottom:1px dotted var(--line)}

/* footer */
.site-footer{height:320px;background:var(--pink);color:var(--white);padding:56px 0 0}
.footer-links{display:flex;justify-content:center;gap:70px}
.footer-links ul{list-style:none}
.footer-links li{font-size:13px;line-height:2.4}
.footer-links li::before{content:"›";margin-right:8px}
.copyright{height:40px;line-height:40px;text-align:center;font-size:11px;color:var(--brown)}
</style>
</head>
<body>
<header class="hero">
  <aside class="sidebar">
    <div class="brand"><span class="brand-dot"></span><span class="brand-name">はるいろ</span></div>
    <ul class="global-nav">
      <li><a href="#">ホーム</a></li>
      <li><a href="#">コンセプト</a></li>
      <li><a href="#">施設紹介・アクセス</a></li>
      <li><a href="#">サービス紹介</a></li>
      <li><a href="#">一日の流れ</a></li>
      <li><a href="#">利用までの流れ</a></li>
      <li><a href="#">ご利用料金</a></li>
      <li><a href="#">よくある質問</a></li>
      <li><a href="#">ケアマネージャー様へ</a></li>
    </ul>
    <div class="contact-box">
      <div class="contact-illust" role="img" aria-label="スタッフのイラスト"></div>
      <p class="contact-note">見学・体験、ご相談は<br>お気軽にお電話ください</p>
      <p class="contact-tel"><svg width="18" height="18" viewBox="0 0 24 24"><path fill="#fff" d="M6.6 10.8a15 15 0 0 0 6.6 6.6l2.2-2.2a1 1 0 0 1 1-.25 11.4 11.4 0 0 0 3.6.57 1 1 0 0 1 1 1V20a1 1 0 0 1-1 1A17 17 0 0 1 3 4a1 1 0 0 1 1-1h3.5a1 1 0 0 1 1 1c0 1.25.2 2.45.57 3.57a1 1 0 0 1-.25 1z"/></svg>072-555-0186</p>
      <a class="contact-btn" href="#">お問い合わせ</a>
    </div>
  </aside>
  <div class="hero-visual" role="img" aria-label="青空と家の前に並ぶ家族と介護スタッフのイラスト">
    <div class="hero-illust"></div>
    <div class="scroll-mark"><span></span>SCROLL</div>
    <nav class="menu-cards">
      <a class="menu-card" href="#"><span class="menu-card-thumb" role="img" aria-label="利用者さまのイラスト"></span><span class="menu-card-body"><span class="menu-card-en">Voice</span><span class="menu-card-title">ご利用者さまの声</span><span class="menu-card-more">詳しく見る ›</span></span></a>
      <a class="menu-card" href="#"><span class="menu-card-thumb" role="img" aria-label="スタッフのイラスト"></span><span class="menu-card-body"><span class="menu-card-en">Recruit</span><span class="menu-card-title">採用情報</span><span class="menu-card-more">詳しく見る ›</span></span></a>
      <a class="menu-card" href="#"><span class="menu-card-thumb" role="img" aria-label="相談する人のイラスト"></span><span class="menu-card-body"><span class="menu-card-en">Question</span><span class="menu-card-title">よくある質問</span><span class="menu-card-more">詳しく見る ›</span></span></a>
      <a class="menu-card" href="#"><span class="menu-card-thumb" role="img" aria-label="イベントのイラスト"></span><span class="menu-card-body"><span class="menu-card-en">Event</span><span class="menu-card-title">イベント</span><span class="menu-card-more">詳しく見る ›</span></span></a>
      <a class="menu-card" href="#"><span class="menu-card-thumb" role="img" aria-label="施設の建物のイラスト"></span><span class="menu-card-body"><span class="menu-card-en">Company</span><span class="menu-card-title">会社概要</span><span class="menu-card-more">詳しく見る ›</span></span></a>
      <a class="menu-card" href="#"><span class="menu-card-thumb" role="img" aria-label="料金案内のイラスト"></span><span class="menu-card-body"><span class="menu-card-en">Price</span><span class="menu-card-title">ご利用料金</span><span class="menu-card-more">詳しく見る ›</span></span></a>
    </nav>
  </div>
</header>

<section class="greeting">
  <h2 class="section-title">ごあいさつ</h2>
  <p class="greeting-text">はるいろは地域の皆さまに寄り添うデイサービスです。<br>ひとりひとりのペースを大切に、笑顔あふれる毎日を。<br>ご家族の皆さまにも安心していただける場所を目指し、<br>スタッフ一同心をこめてお迎えいたします。<br>まずはお気軽に見学・体験にお越しください。<br>皆さまのお越しを心よりお待ちしております。</p>
  <div class="greeting-photos">
    <div class="greeting-photo" style="background:linear-gradient(#d9c3a9,#f1e4d2)" role="img" aria-label="スタッフの写真"></div>
    <div class="greeting-photo" style="background:linear-gradient(#b68a64,#e2c8a6)" role="img" aria-label="施設内の写真"></div>
    <div class="greeting-photo" style="background:linear-gradient(#c6b9a8,#ece4d8)" role="img" aria-label="食堂の写真"></div>
    <div class="greeting-photo" style="background:linear-gradient(#8d6e57,#cdb49a)" role="img" aria-label="くつろぎスペースの写真"></div>
    <div class="greeting-photo" style="background:linear-gradient(#c98d5f,#efd2b0)" role="img" aria-label="お食事の写真"></div>
  </div>
</section>

<section class="news">
  <h2 class="section-title">お知らせ ＆ ブログ</h2>
  <div class="news-list">
    <article class="news-item"><div class="news-thumb" role="img" aria-label="車椅子で散歩する写真"></div><p class="news-text">秋の散歩イベントを開催しました。皆さまと紅葉を楽しみました。</p><p class="news-date">2017.10.20</p></article>
    <article class="news-item"><div class="news-thumb" role="img" aria-label="屋外でくつろぐ写真"></div><p class="news-text">年末年始の営業日についてのお知らせを掲載しました。</p><p class="news-date">2017.10.12</p></article>
    <article class="news-item"><div class="news-thumb" role="img" aria-label="介護スタッフの写真"></div><p class="news-text">新しいスタッフが加わりました。よろしくお願いいたします。</p><p class="news-date">2017.10.05</p></article>
    <article class="news-item"><div class="news-thumb" role="img" aria-label="公園を歩く写真"></div><p class="news-text">体験利用の受付を行っています。お気軽にご相談ください。</p><p class="news-date">2017.09.28</p></article>
  </div>
  <div class="news-actions"><a class="pill-btn" href="#">お知らせ一覧</a><a class="pill-btn" href="#">ブログ一覧</a></div>
</section>

<section class="access">
  <h2 class="section-title">アクセス</h2>
  <div class="access-body">
    <div class="access-map" role="img" aria-label="施設周辺の地図"></div>
    <table class="access-table">
      <tr><th>施設名</th><td>デイサービスセンター はるいろ</td></tr>
      <tr><th>所在地</th><td>大阪府はるいろ市さくら町1-2-3</td></tr>
      <tr><th>電話番号</th><td>072-555-0186</td></tr>
      <tr><th>FAX番号</th><td>072-555-0187</td></tr>
      <tr><th>営業時間</th><td>9:00〜17:00</td></tr>
      <tr><th>定休日</th><td>日曜日</td></tr>
      <tr><th>駐車場</th><td>あり（5台）</td></tr>
      <tr><th>送迎</th><td>市内全域で送迎いたします</td></tr>
    </table>
  </div>
</section>

<footer class="site-footer">
  <div class="footer-links">
    <ul><li>ホーム</li><li>コンセプト</li><li>サービス紹介</li></ul>
    <ul><li>施設紹介・アクセス</li><li>一日の流れ</li><li>イベント</li></ul>
    <ul><li>利用までの流れ</li><li>ご利用料金</li><li>よくある質問</li></ul>
    <ul><li>ケアマネージャー様へ</li><li>採用情報</li><li>会社概要</li></ul>
    <ul><li>ブログ</li><li>お知らせ</li><li>お問い合わせ</li></ul>
  </div>
</footer>
<p class="copyright">Copyright © デイサービスセンター はるいろ All Rights Reserved.</p>
</body>
</html>
```